TalkNest Needs a Brochure Design

We need a brochure (sent as an e-mail message and via mail), to market our professional development seminars. We provide seminars related to autism and non-verbal communication. Brochure should have certain information (see Must Have Priorities) and be designed for target market.

Please submit only 2-3 of your best designs.
Updates

I have added a word file with detail information about the seminar. We want a design that can be sent both as e-mail and regular mail. A 8 x 10 design that can be folded and mailed will meet our requirements. We are hoping that we will be able to send the one page as an e-mail and the back can be used for advertisement.

Target Market(s)

Physicians, Speech-Language Pathologists, Occupational Therapist, Early Intervention Specialists, Special Educators.

Industry/Entity Type

Communication

Font styles to use
Sans Serif

Colors
3176b5
33b7a4
f68d4d

Requirements
Must have
• See the attached file. In addition the brochure must have:
1 Logo for academic accreditation and CEU information.
2. Registration Fees and how to register.
Nice to have
• Photographs.

```html
<!DOCTYPE html>
<html lang="en">
<head>
<meta charset="utf-8">
<title>TalkNest Seminar Brochure – Mobile Technology in Autism</title>
<link href="https://fonts.googleapis.com/css2?family=Open+Sans:wght@300;400;600;700&display=swap" rel="stylesheet">
<style>
  :root {
    --sky: #eef5f8;
    --white: #ffffff;
    --blue: #3176b5;
    --band-blue: #1b8ccc;
    --teal: #33b7a4;
    --orange: #f68d4d;
    --ink: #1d1d1f;
    --slate: #44474c;
    --dash: #3a3a3a;
    --rule: rgba(255,255,255,.45);
  }
  * { box-sizing: border-box; margin: 0; padding: 0; }
  html, body { width: 982px; height: 1200px; overflow: hidden; background: var(--white); }
  body { font-family: "Open Sans", Arial, sans-serif; color: var(--ink); }

  .brochure { position: relative; width: 982px; height: 1200px; overflow: hidden; }

  /* Hero */
  .hero { position: absolute; left: 0; top: 0; width: 982px; height: 710px;
    background: radial-gradient(circle at 52% 38%, #ffffff 0%, var(--sky) 60%, #e6f0f5 100%); }
  .connectors { position: absolute; left: 0; top: 0; width: 982px; height: 710px; }

  .brand-card { position: absolute; left: 43px; top: 20px; width: 318px; height: 120px;
    background: var(--white); border-radius: 14px; display: flex; align-items: center;
    gap: 16px; padding-left: 30px; box-shadow: 0 2px 8px rgba(0,0,0,.05); }
  .brand-mark { width: 44px; height: 44px; background: var(--blue); border-radius: 4px; }
  .brand-name { font-weight: 600; font-size: 36px; color: var(--blue); letter-spacing: -.5px; }

  /* Illustration areas: soft single-tone fills */
  .art { position: absolute; border-radius: 50%; }
  .art-person-left  { left: 112px; top: 178px; width: 84px; height: 84px; background: radial-gradient(circle, #d9dde0, #c3c8cc); }
  .art-thumb        { left: 438px; top: 56px;  width: 72px; height: 72px; background: radial-gradient(circle, #a9dfe8, #7fcbd9); }
  .art-heart        { left: 604px; top: 30px;  width: 74px; height: 74px; background: radial-gradient(circle, #ef8a84, #e4625b); }
  .art-person-right { left: 780px; top: 96px;  width: 84px; height: 84px; background: radial-gradient(circle, #d6d9dc, #bfc4c8); }
  .art-binoculars   { left: 556px; top: 208px; width: 84px; height: 70px; background: radial-gradient(circle, #8a9097, #6c727a); }
  .art-book         { left: 692px; top: 212px; width: 68px; height: 78px; border-radius: 10px; background: radial-gradient(circle, #f6cf7d, #efba52); }
  .art-chat         { left: 160px; top: 380px; width: 74px; height: 64px; border-radius: 12px; background: radial-gradient(circle, #8d9096, #73767c); }

  .art-tablet { left: 268px; top: 384px; width: 440px; height: 326px; border-radius: 22px 22px 0 0;
    background: radial-gradient(ellipse at 50% 45%, #5b5e63 0%, var(--slate) 70%, #3a3d41 100%); }

  .seminar-title { position: absolute; left: 292px; top: 416px; width: 392px; text-align: center;
    color: var(--white); font-weight: 300; line-height: 1; text-transform: uppercase; }
  .seminar-title .t-large { display: block; font-size: 44px; letter-spacing: 1px; }
  .seminar-title .t-small { display: block; font-size: 18px; margin-top: 14px; letter-spacing: .5px; }
  .seminar-title .t-in { display: block; font-size: 18px; margin-top: 4px; }
  .seminar-title .t-hero { display: block; font-size: 66px; margin-top: 8px; letter-spacing: 1px; }

  .event-card { position: absolute; left: 239px; top: 198px; width: 256px; height: 152px;
    background: var(--teal); border-radius: 14px; color: var(--white); padding: 16px 16px; }
  .event-card .label { font-size: 17px; font-weight: 400; line-height: 1.1; }
  .event-card .value { font-size: 17px; font-weight: 700; line-height: 1.2; margin-bottom: 10px; }

  .speaker { position: absolute; right: 42px; top: 228px; text-align: right; font-weight: 700; line-height: 1.15; }
  .speaker .label { font-size: 20px; color: var(--ink); }
  .speaker .name { font-size: 20px; color: var(--orange); }

  .instructor { position: absolute; left: 722px; top: 302px; width: 220px; }
  .instructor h3 { text-align: right; font-size: 15px; font-weight: 700; line-height: 1.2; }
  .instructor p { font-size: 13.2px; line-height: 1.32; text-align: justify; text-indent: 24px; }

  /* Blue band */
  .details { position: absolute; left: 0; top: 710px; width: 982px; height: 298px; background: var(--band-blue);
    color: var(--white); display: flex; gap: 21px; padding: 24px 38px 0 43px; }
  .details h2 { font-size: 19px; font-weight: 700; margin-bottom: 2px; }
  .course, .outcomes { width: 440px; }
  .course p, .outcomes p, .outcomes ol { font-size: 14.8px; line-height: 1.4; }
  .outcomes ol { list-style: none; }
  .outcomes li { padding-left: 17px; text-indent: -17px; }

  /* Footer */
  .footer { position: absolute; left: 0; top: 1008px; width: 982px; height: 192px; background: var(--teal); }
  .accreditation { position: absolute; left: 41px; top: 26px; width: 285px; height: 138px; background: var(--white);
    padding: 8px 10px; display: flex; gap: 8px; }
  .accreditation .badge { flex: 0 0 92px; height: 76px; border: 2px solid #555; background: #f3f3f3; }
  .accreditation p { font-size: 7.6px; line-height: 1.32; color: #333; }
  .footer-col { position: absolute; top: 26px; width: 250px; }
  .footer-col h4 { color: var(--white); font-size: 17px; font-weight: 400; letter-spacing: .3px; margin-bottom: 18px; }
  .footer-col .rule { display: block; height: 1px; background: var(--rule); margin-bottom: 22px; }
  .register { left: 362px; }
  .fees { left: 657px; }
</style>
</head>
<body>
<main class="brochure">
  <section class="hero">
    <svg class="connectors" viewBox="0 0 982 710" aria-hidden="true">
      <g fill="none" stroke="var(--dash)" stroke-width="1.6" stroke-dasharray="5 6">
        <path d="M322 150 C 330 175, 350 190, 360 198"/>
        <path d="M474 128 C 470 155, 470 178, 462 198"/>
        <path d="M640 104 C 620 140, 600 180, 598 208"/>
        <path d="M820 182 C 805 225, 795 250, 762 252"/>
        <path d="M152 264 C 170 315, 200 335, 212 345"/>
        <path d="M234 430 C 255 455, 270 468, 268 470"/>
        <path d="M440 352 C 445 368, 448 378, 452 384"/>
        <path d="M748 292 C 738 340, 726 370, 716 384"/>
      </g>
    </svg>

    <div class="brand-card">
      <span class="brand-mark" aria-hidden="true"></span>
      <span class="brand-name">TalkNest</span>
    </div>

    <div class="art art-person-left" role="img" aria-label="Avatar icon of a woman"></div>
    <div class="art art-thumb" role="img" aria-label="Thumbs-up icon"></div>
    <div class="art art-heart" role="img" aria-label="Heart icon"></div>
    <div class="art art-person-right" role="img" aria-label="Avatar icon of a man"></div>
    <div class="art art-binoculars" role="img" aria-label="Binoculars icon"></div>
    <div class="art art-book" role="img" aria-label="Notebook icon"></div>
    <div class="art art-chat" role="img" aria-label="Speech bubble icon"></div>
    <div class="art art-tablet" role="img" aria-label="Illustration of hands holding a tablet"></div>

    <h1 class="seminar-title">
      <span class="t-large">Mobile</span>
      <span class="t-large">Technology</span>
      <span class="t-small">to support communication</span>
      <span class="t-in">in</span>
      <span class="t-hero">Autism</span>
    </h1>

    <div class="event-card">
      <div class="label">DATE:</div>
      <div class="value">September 20, 2014</div>
      <div class="label">LOCATION:</div>
      <div class="value">740 W Harbor Street,<br>Chicago, IL 60610</div>
    </div>

    <div class="speaker">
      <div class="label">SPEAKER:</div>
      <div class="name">ARUN MEHRA,<br>Ph.D., CCC-SLP</div>
    </div>

    <div class="instructor">
      <h3>INSTRUCTOR:</h3>
      <p>Arun Mehra is an Associate Professor of Communication Disorders at Prairie Ridge University. He earned his doctorate from Lakeview University. He has working experience in diverse settings including private practice, hospitals, long-term residential settings and integrated school-settings. His areas of research interest are: assistive technology, early language intervention, and reading disabilities. He has over 30 publications and over 100 presentations at national and international scientific meetings. He is a consulting editor for Journal of Assistive Communication.</p>
    </div>
  </section>

  <section class="details">
    <div class="course">
      <h2>COURSE DESCRIPTION:</h2>
      <p>With the current availability of mobile technology (e.g., Slate tablet, Orbit phone) individuals with autism have many options available for communication. This course focused on visual support, accessibility, and language learning through mobile technology. Compared specialized AAC “apps” and assessed contemporary evidence for effective use of mobile technology by children with autism to enhance their communication skills.</p>
    </div>
    <div class="outcomes">
      <h2>LEARNER’S OUTCOMES:</h2>
      <p>As a result of this seminar, the participant will be able to:</p>
      <ol>
        <li>1. summarize issues related to information processing, visual attention, and visual support in children with autism.</li>
        <li>2. decide about accessibility of mobile technology by children with autism.</li>
        <li>3. integrate language learning strategies using mobile technology for children with autism.</li>
        <li>4. compare contemporary specialized AAC “apps” for children with autism.</li>
        <li>5. assess contemporary evidence for effectiveness of mobile technology by children with autism.</li>
      </ol>
    </div>
  </section>

  <footer class="footer">
    <div class="accreditation">
      <div class="badge" role="img" aria-label="Approved continuing education provider badge"></div>
      <p><strong>Prairie Ridge University</strong> is approved by the Continuing Education Board of the National Speech and Hearing Council (NSHC) to provide continuing education activities in speech-language pathology and audiology. <strong>See course information for number of NSHC CEUs, instructional level and content area.</strong> NSHC CE Provider approval does not imply endorsement of course content, specific products or clinical procedures.</p>
    </div>
    <div class="footer-col register">
      <h4>HOW TO REGISTER</h4>
      <span class="rule"></span><span class="rule"></span><span class="rule"></span><span class="rule"></span>
    </div>
    <div class="footer-col fees">
      <h4>REGISTRATION FEES</h4>
      <span class="rule"></span><span class="rule"></span><span class="rule"></span><span class="rule"></span>
    </div>
  </footer>
</main>
</body>
</html>
```